Radiology Department needs a series of 3 facebook posts - similar design

We need a series of 3 posts for our facebook page, each one presenting the activity of one of 3 physicians.
The main design elements can be the same, the only thing that will change between posts will be the field of activity and name of the physician and the representative image of its activity.
If needed the design elements can be slightly different between posts for better adjustment to the representative images.
You can find as an attachment:
- Manual of institutional identity of the Hospital (Velmor Clinica)
- Our facebook cover page
- Our department video
- The representative images for each post, identified with the name of each physician
- The Institutional identity manual with the logo of "Brisa Medical School" - just for Dr Tomas Brandilo post.
So, each one of the three posts should state the name and field of activity of each physician, including somehow the corresponding representative image, and should have background innovative design elements.
Post 1:
Name of the physician: Prof. Doutor Rui Castelvo
Field of activity: Imagiologia Reumatológica e do Sistema Músculo-Esquelético
Image as an attachment
Post 2:
Name of the physician: Prof.ª Doutora Inês Barroca
Field of activity: Imagiologia Cardíaca
Image as an attachment
Post 3:
Name of the physician: Dr. Tomas Lupo
Field of activity: Tese de Doutoramento em Curso - Identificação da Lesão Cartilagínea Precoce. Com orientação do Prof. Doutor Rui Castelvo e Prof.ª Doutora Inês Sofia Carvalhal.
Image as an attachment
Just for Dr Tomas Lupo, the logo of Brisa Medical School should also be included (please check the corresponding institutional identity manual that was just added in documents).
Updates

Just for Dr Tomas Brandilo, the logo of Brisa Medical School should also be included (please check the corresponding institutional identity manual that was just added in documents).

Please note that we are just looking for 3 facebook POSTS, not facebook cover page, thanks.

Please kindly note that we are looking for facebook POST and NOT facebook cover page.

Target Market(s)

General Population

Industry/Entity Type

Health

Font styles to use
Other font styles liked:
• Check manual of institutional identity and try to approach if appropriate

Requirements
Must have
• Check project description.
Nice to have
• If the designer finds appropriate, the logo of the Hospital would be nice in all the three posts, the most simple one just stating "VelmorClinica" - please check the attached manual of institutional identity

```html
<!DOCTYPE html>
<html lang="pt">
<head>
<meta charset="utf-8">
<title>Imagiologia Reumatológica – VelmorClinica</title>
<link rel="stylesheet" href="https://fonts.googleapis.com/css2?family=Poppins:wght@400;500;600;700&display=swap">
<style>
  :root {
    --teal: #0f5e6f;
    --teal-dark: #0b4a5b;
    --yellow: #f9b91c;
    --white: #ffffff;
    --scan-dark: #050505;
    --scan-mid: #3a3a3a;
  }
  * { margin: 0; padding: 0; box-sizing: border-box; }
  html, body { width: 1200px; height: 1200px; overflow: hidden; background: var(--teal); }
  .post {
    position: relative; width: 1200px; height: 1200px; overflow: hidden;
    background: var(--teal); font-family: "Poppins", sans-serif; color: var(--white);
  }
  .post__shapes { position: absolute; inset: 0; }
  .brand {
    position: absolute; left: 56px; top: 263px; display: flex; align-items: center; gap: 18px;
  }
  .brand__dot { width: 76px; height: 76px; border-radius: 50%; background: var(--white); }
  .brand__name { font-size: 33px; font-weight: 600; color: var(--white); }
  .specialty {
    position: absolute; left: 56px; top: 392px; width: 600px;
    font-size: 59px; line-height: 77px; font-weight: 700; letter-spacing: -0.3px;
  }
  .contact { position: absolute; left: 70px; top: 850px; }
  .contact__label {
    display: flex; align-items: center; gap: 20px;
    font-size: 24px; font-weight: 400; letter-spacing: 0.5px;
  }
  .contact__label::after { content: ""; width: 44px; height: 3px; background: var(--yellow); }
  .contact__phone {
    margin-top: 12px; font-size: 49px; font-weight: 700; color: var(--yellow); letter-spacing: 0.5px;
  }
  .coordinator {
    position: absolute; left: 889px; top: 999px; transform: translateX(-50%);
    display: flex; align-items: center; gap: 18px; font-size: 33px; font-weight: 500; white-space: nowrap;
  }
  .coordinator::before, .coordinator::after {
    content: ""; width: 50px; height: 3px; background: var(--white);
  }
  .physician {
    position: absolute; left: 542px; top: 1068px; width: 658px; height: 92px;
    background: var(--yellow); display: flex; align-items: center; justify-content: center;
    font-size: 35px; font-weight: 600; color: var(--white); padding-right: 40px;
  }
</style>
</head>
<body>
  <main class="post">
    <svg class="post__shapes" viewBox="0 0 1200 1200" width="1200" height="1200">
      <defs>
        <radialGradient id="scan-tone" cx="50%" cy="45%" r="55%">
          <stop offset="0" stop-color="var(--scan-mid)"/>
          <stop offset="1" stop-color="var(--scan-dark)"/>
        </radialGradient>
      </defs>
      <g class="white-bands" stroke="var(--white)" stroke-width="120">
        <line x1="400" y1="-40" x2="889" y2="584"/>
        <line x1="360" y1="1240" x2="889" y2="584"/>
        <line x1="1240" y1="290" x2="889" y2="584"/>
        <line x1="1240" y1="820" x2="889" y2="584"/>
      </g>
      <polygon class="chevron-edge" fill="var(--yellow)" points="250,0 312,0 682,530 312,1200 250,1200 620,530"/>
      <polygon class="chevron-panel" fill="var(--teal-dark)" points="0,0 254,0 624,530 254,1200 0,1200"/>
      <ellipse class="accent-ellipse" cx="889" cy="174" rx="105" ry="114" fill="var(--yellow)"/>
      <circle class="scan-frame" cx="889" cy="584" r="298" fill="var(--white)"/>
      <circle class="scan-image" cx="889" cy="584" r="285" fill="url(#scan-tone)"
              role="img" aria-label="Angiografia por ressonância magnética das duas mãos, em tons de cinzento sobre fundo preto"/>
    </svg>

    <div class="brand">
      <span class="brand__dot"></span>
      <span class="brand__name">VelmorClinica</span>
    </div>

    <h1 class="specialty">Imagiologia<br>Reumatológica<br>e do Sistema<br>Músculo-<br>Esquelético</h1>

    <div class="contact">
      <p class="contact__label">CONTACTO</p>
      <p class="contact__phone">252 400 718</p>
    </div>

    <p class="coordinator">Coordenador</p>
    <p class="physician">Prof. Doutor Rui Castelvo</p>
  </main>
</body>
</html>
```